[AMAZING DESIGN NEEDED] Women's Fishing Squeeze Page

I need a professional design for a landing page that is going to collect email addresses.

You can use the creatives already on the page or you can pull images from the facebook/instagram pages.
https://www.facebook.com/LakesLuresBoots
https://www.instagram.com/lakesluresandboots/

This is the page that needs designed: https://lakesluresandboots.example/email-opt-in/

See attached for examples.

Target Market(s)

Women who like to go fishing

Industry/Entity Type

Fishing

Number of Pages Required

1 page

Font styles to use
Sans Serif

Requirements
Must have
• excellent design. Call to actions.

```html
<!DOCTYPE html>
<html lang="en">
<head>
<meta charset="utf-8">
<title>Lakes, Lures &amp; Boots — Email Sign Up</title>
<link rel="stylesheet" href="https://fonts.googleapis.com/css2?family=Montserrat:wght@300;400;600;700;800&family=Roboto:wght@400;500&family=Libre+Baskerville:wght@700&display=swap">
<style>
  :root {
    --sand: #cdbcab;
    --brown-dark: #4a3a2c;
    --brown-text: #5b4636;
    --brown-link: #86684f;
    --coral: #ec5b3b;
    --coral-soft: #f3a48f;
    --coral-tint: #fdeee9;
    --teal: #2aa7a8;
    --field: #ececec;
    --ink: #111111;
    --muted: #6b6b6b;
    --white: #ffffff;
  }
  * { box-sizing: border-box; margin: 0; padding: 0; }
  html, body { width: 1052px; height: 1200px; overflow: hidden; background: var(--white); }
  body { position: relative; font-family: "Roboto", sans-serif; }
  a { color: inherit; text-decoration: none; }

  /* Header */
  .site-header { position: absolute; left: 0; top: 0; width: 1052px; height: 201px; background: var(--sand); }
  .utility-bar { position: absolute; right: 20px; top: 9px; display: flex; align-items: center; gap: 13px; font-weight: 500; font-size: 8.6px; color: var(--brown-text); text-transform: uppercase; }
  .utility-bar .or { text-transform: lowercase; font-weight: 400; margin: 0 -9px; }
  .social-squares { display: flex; gap: 9px; padding-right: 8px; border-right: 1px solid var(--brown-text); height: 13px; align-items: center; }
  .social-squares span { width: 12px; height: 12px; background: var(--brown-text); border-radius: 2px; display: block; }
  .brand { position: absolute; left: 0; width: 100%; top: 88px; text-align: center; font-family: "Montserrat", sans-serif; font-weight: 700; font-size: 17px; color: var(--teal); letter-spacing: 0.5px; }
  .main-nav { position: absolute; left: 0; width: 100%; top: 177px; display: flex; justify-content: center; gap: 20px; font-weight: 500; font-size: 9.4px; color: var(--brown-text); text-transform: uppercase; }
  .main-nav .caret { font-size: 7px; margin-left: 4px; }

  /* Sign up */
  .signup { position: absolute; left: 60px; top: 325px; width: 430px; text-align: center; }
  .signup-title { font-family: "Montserrat", sans-serif; font-weight: 800; font-size: 29px; color: var(--coral); letter-spacing: 0.3px; }
  .signup-offer { margin-top: 14px; font-family: "Montserrat", sans-serif; font-weight: 700; font-size: 16px; color: var(--ink); }
  .signup-note { margin-top: 2px; font-family: "Montserrat", sans-serif; font-weight: 400; font-size: 14px; color: var(--ink); }
  .signup-form { position: absolute; left: 136px; top: 456px; width: 278px; }
  .field { display: block; width: 278px; height: 31px; background: var(--field); padding: 0 11px; font-family: "Montserrat", sans-serif; font-size: 14px; color: #888; margin-bottom: 30px; line-height: 31px; }
  .field:nth-child(2) { margin-bottom: 29px; }
  .privacy { position: absolute; left: 60px; top: 636px; width: 430px; text-align: center; font-family: "Montserrat", sans-serif; font-weight: 300; font-size: 14px; line-height: 18px; color: var(--muted); }
  .privacy a { text-decoration: underline; }
  .cta { position: absolute; left: 145px; top: 698px; width: 261px; height: 62px; background: var(--coral); border-radius: 3px; color: var(--white); font-family: "Montserrat", sans-serif; font-weight: 700; font-size: 15px; display: flex; align-items: center; justify-content: center; letter-spacing: 0.2px; }

  .ornament-area { position: absolute; left: 478px; top: 325px; width: 145px; height: 115px; border-radius: 50%; background: radial-gradient(ellipse at center, var(--coral-tint) 0%, rgba(253,238,233,0) 70%); }
  .hero-photo { position: absolute; left: 600px; top: 272px; width: 478px; height: 478px; border-radius: 50%; background: linear-gradient(200deg, var(--coral) 0%, var(--coral) 55%, #e4704f 100%); }

  /* Footer */
  .site-footer { position: absolute; left: 0; top: 888px; width: 1052px; height: 312px; background: var(--sand); color: var(--brown-link); }
  .footer-heading { font-family: "Libre Baskerville", serif; font-weight: 700; font-size: 8.6px; color: var(--brown-text); }
  .connect { position: absolute; right: 176px; top: 20px; text-align: right; }
  .connect .social-squares { border: none; justify-content: flex-end; margin-top: 14px; padding: 0; gap: 10px; }
  .footer-col { position: absolute; top: 103px; }
  .footer-col ul { list-style: none; margin-top: 10px; font-size: 8.6px; line-height: 13.2px; }
  .col-nav { left: 176px; } .col-cat { left: 294px; } .col-info { left: 414px; } .col-news { left: 532px; width: 230px; }
  .col-info .region { font-style: italic; }
  .col-info .phone { color: var(--brown-text); font-weight: 500; }
  .news-text { margin-top: 10px; font-size: 8.6px; line-height: 13.2px; }
  .news-form { display: flex; gap: 8px; margin-top: 14px; }
  .news-input { width: 134px; height: 27px; background: var(--white); border: 1px solid #bbb; font-size: 8.4px; color: #333; padding: 0 8px; line-height: 25px; }
  .news-button { width: 83px; height: 27px; background: var(--brown-dark); color: var(--white); font-family: "Libre Baskerville", serif; font-weight: 700; font-size: 8.6px; display: flex; align-items: center; justify-content: center; border-radius: 2px; }
  .payments { position: absolute; left: 535px; top: 234px; display: flex; gap: 10px; }
  .payments span { width: 32px; height: 16px; background: var(--brown-text); opacity: 0.75; border-radius: 3px; display: block; }
  .copyright { position: absolute; left: 176px; top: 279px; font-size: 7.2px; color: var(--brown-link); }
</style>
</head>
<body>
  <header class="site-header">
    <div class="utility-bar">
      <div class="social-squares"><span></span><span></span></div>
      <a href="#">Search</a>
      <a href="#">Gift Certificates</a>
      <a href="#">Sign in</a><span class="or">or</span><a href="#">Register</a>
      <a href="#">Cart</a>
    </div>
    <div class="brand">Lakes, Lures &amp; Boots</div>
    <nav class="main-nav">
      <a href="#">Clothing<span class="caret">&#8964;</span></a>
      <a href="#">Hats</a>
      <a href="#">Bundles</a>
      <a href="#">Accessories &amp; Stickers</a>
      <a href="#">Jewelry</a>
      <a href="#">Clearance</a>
    </nav>
  </header>

  <section class="signup">
    <h1 class="signup-title">SIGN UP TODAY</h1>
    <p class="signup-offer">And Receive 15% Off Your Next Order</p>
    <p class="signup-note">You Will Also stay Updated On Our New Products</p>
  </section>

  <form class="signup-form">
    <div class="field">First Name</div>
    <div class="field">Last Name</div>
    <div class="field">Email</div>
  </form>

  <p class="privacy">All information collected will be used in accordance<br>with our <a href="#">Privacy Policy</a></p>
  <a class="cta" href="#">YES! HOOK ME UP!</a>

  <div class="ornament-area" role="img" aria-label="Decorative dashed looping fishing line ornament in coral"></div>

  <div class="hero-photo" role="img" aria-label="Photo of a woman angler in a cap and waders holding a small trout, with her dog beside her, set inside an orange circle"></div>

  <footer class="site-footer">
    <div class="connect">
      <div class="footer-heading">Connect With Us</div>
      <div class="social-squares"><span></span><span></span></div>
    </div>
    <div class="footer-col col-nav">
      <div class="footer-heading">Navigate</div>
      <ul><li>Trips</li><li>Shipping &amp; Returns</li><li>Contact Us</li><li>Blog</li><li>Sitemap</li></ul>
    </div>
    <div class="footer-col col-cat">
      <div class="footer-heading">Categories</div>
      <ul><li>Clothing</li><li>Hats</li><li>Bundles</li><li>Accessories &amp; Stickers</li><li>Jewelry</li><li>Clearance</li></ul>
    </div>
    <div class="footer-col col-info">
      <div class="footer-heading">Info</div>
      <ul><li class="region">Montana</li><li class="phone">Call us at 4065550147</li></ul>
    </div>
    <div class="footer-col col-news">
      <div class="footer-heading">Subscribe to our newsletter</div>
      <p class="news-text">Get the latest updates on new products and upcoming<br>sales</p>
      <div class="news-form">
        <div class="news-input">Your email address</div>
        <div class="news-button">Subscribe</div>
      </div>
    </div>
    <div class="payments" aria-label="Accepted payment methods"><span></span><span></span><span></span><span></span><span></span></div>
    <div class="copyright">© 2021 Lakes, Lures &amp; Boots</div>
  </footer>
</body>
</html>
```